Social Media Cover and Profile

We already have our own logo. We just need a fresh design on our social media pages. We are not happy with our current designs. We would like to incorporate our YIKE billboard and the colors are blue (#05143f) and white. You can also incorporate silver as well. We are a family law office (Divorce and Custody) We no longer want to incorporate the Spire of Dunvale photo that we are currently using. You can look at our Facebook page; The Law Office of Miles T. Hadley.

Target Market(s)

Potential Clients

Industry/Entity Type

Family Law

Logo Text

Our Logo Is The Law Office of Miles T. Hadley with the Sheild

Requirements
Must have
• Text to include:
Central Pennslyvania's Premier Family Law Firm

Ability to be resized to and used as all images in social media, including but not limited to: Youtube Channel art, Facebook Cover and Profile.
Nice to have
• Darker color but we are open to "bright" ideas.

```html
<!DOCTYPE html>
<html lang="en">
<head>
<meta charset="UTF-8">
<title>YIKE – Family Law Cover</title>
<link rel="stylesheet" href="https://fonts.googleapis.com/css2?family=Arimo:wght@700&family=DM+Serif+Text&display=swap">
<style>
  :root {
    --page-bg: #f2f2f2;
    --cover-light: #ededed;
    --cover-mid: #dedede;
    --glow: #ffffff;
    --silver-light: #d9d9d9;
    --silver-mid: #a6a6a6;
    --silver-dark: #767676;
    --silver-edge: #c4c4c4;
    --navy: #05143f;
  }
  * { margin: 0; padding: 0; box-sizing: border-box; }
  html, body {
    width: 1200px;
    height: 720px;
    overflow: hidden;
    background: var(--page-bg);
  }
  .cover {
    position: absolute;
    left: 52px;
    top: 155px;
    width: 1101px;
    height: 420px;
    overflow: hidden;
  }
  .cover__art {
    position: absolute;
    inset: 0;
    width: 100%;
    height: 100%;
  }
  .cover__wordmark {
    font-family: "Arimo", Arial, sans-serif;
    font-weight: 700;
    font-size: 256px;
    letter-spacing: 8px;
  }
  .cover__tagline {
    font-family: "DM Serif Text", Georgia, serif;
    font-size: 33px;
  }
</style>
</head>
<body>
  <section class="cover">
    <svg class="cover__art" viewBox="0 0 1101 420">
      <defs>
        <radialGradient id="coverBase" cx="50%" cy="45%" r="75%">
          <stop offset="0%" stop-color="var(--cover-light)"/>
          <stop offset="100%" stop-color="var(--cover-mid)"/>
        </radialGradient>
        <radialGradient id="softGlow">
          <stop offset="0%" stop-color="var(--glow)" stop-opacity="0.85"/>
          <stop offset="60%" stop-color="var(--glow)" stop-opacity="0.35"/>
          <stop offset="100%" stop-color="var(--glow)" stop-opacity="0"/>
        </radialGradient>
        <linearGradient id="silverFill" x1="0" y1="0" x2="0" y2="1">
          <stop offset="0%" stop-color="var(--silver-light)"/>
          <stop offset="45%" stop-color="var(--silver-mid)"/>
          <stop offset="100%" stop-color="var(--silver-dark)"/>
        </linearGradient>
      </defs>

      <g role="img" aria-label="Soft silver backdrop with floating white hearts and sparkles">
        <rect width="1101" height="420" fill="url(#coverBase)"/>
        <circle cx="60" cy="70" r="70" fill="url(#softGlow)"/>
        <circle cx="180" cy="20" r="90" fill="url(#softGlow)"/>
        <circle cx="20" cy="215" r="70" fill="url(#softGlow)"/>
        <circle cx="140" cy="290" r="70" fill="url(#softGlow)"/>
        <circle cx="40" cy="400" r="50" fill="url(#softGlow)"/>
        <circle cx="440" cy="50" r="60" fill="url(#softGlow)"/>
        <circle cx="602" cy="20" r="90" fill="url(#softGlow)"/>
        <circle cx="820" cy="20" r="80" fill="url(#softGlow)"/>
        <circle cx="990" cy="70" r="80" fill="url(#softGlow)"/>
        <circle cx="980" cy="300" r="75" fill="url(#softGlow)"/>
        <circle cx="1075" cy="370" r="55" fill="url(#softGlow)"/>
        <circle cx="588" cy="400" r="80" fill="url(#softGlow)"/>
        <circle cx="260" cy="400" r="40" fill="url(#softGlow)"/>
      </g>

      <text class="cover__wordmark" x="549" y="286" text-anchor="middle"
            fill="url(#silverFill)" stroke="var(--silver-edge)" stroke-width="3">YIKE</text>

      <text class="cover__tagline" x="549" y="336" text-anchor="middle"
            textLength="687" lengthAdjust="spacingAndGlyphs"
            fill="var(--navy)">Central Pennslyvania's Premier Family Law Firm</text>
    </svg>
  </section>
</body>
</html>
```